Webdesign für Brunnkamp Maler
Zielgruppe
Maler- und Bodenlegerarbeiten, Farbenherstellung, Fachmarkt
ZieIgruppe sind alle, die Fraben und/oder die Dienstleistungen der Firma benötigen
Aufgabenstellung
dem Kunde gefällt die Seite http://www.maler-voskuhl-beispiel.de/
bitte alle Uploads beachten
eigene Bilder und Stockmaterial

```html
<!DOCTYPE html>
<html lang="de">
<head>
<meta charset="utf-8">
<title>Brunnkamp Maler – Kontakt</title>
<link href="https://fonts.googleapis.com/css2?family=Oxygen:wght@400;700&family=Varela+Round&display=swap" rel="stylesheet">
<style>
  :root {
    --brand-blue: #003a94;
    --brand-pink: #e0135c;
    --text-dark: #2b2b2b;
    --text-muted: #9a9a9a;
    --field-border: #c9c9c9;
    --white: #ffffff;
  }
  * { box-sizing: border-box; margin: 0; padding: 0; }
  html, body { width: 1200px; height: 502px; overflow: hidden; }
  body {
    position: relative;
    background: var(--brand-blue);
    font-family: "Oxygen", sans-serif;
    color: var(--text-dark);
  }
  .site-header {
    position: absolute; left: 0; top: 0; width: 1200px; height: 64px;
    background: var(--white);
  }
  .site-header::before {
    content: ""; position: absolute; left: 0; top: 0; right: 0; height: 10px;
    background: linear-gradient(rgba(0,0,0,0.35), rgba(0,0,0,0));
  }
  .brand-name {
    position: absolute; left: 35px; top: 18px;
    font-family: "Oxygen", sans-serif; font-weight: 700; font-size: 20px;
    color: var(--brand-blue); line-height: 26px;
  }
  .main-nav { position: absolute; top: 23px; left: 468px; display: flex; gap: 35px; }
  .main-nav a {
    font-size: 14px; color: var(--text-dark); text-decoration: none; line-height: 18px;
    padding-bottom: 2px;
  }
  .main-nav a.is-active { border-bottom: 1.5px solid var(--text-dark); }
  .cta-button {
    position: absolute; left: 967px; top: 16px; width: 188px; height: 32px;
    background: var(--brand-pink); color: var(--white); border-radius: 3px;
    font-size: 14px; line-height: 32px; text-align: center;
  }
  .content-panel {
    position: absolute; left: 102px; top: 64px; width: 997px; height: 438px;
    background: var(--white);
  }
  .page-title {
    position: absolute; left: 0; right: 0; top: 94px; text-align: center;
    font-family: "Varela Round", sans-serif; font-weight: 400; font-size: 31px;
    color: var(--brand-pink); line-height: 40px;
  }
  .field-label {
    position: absolute; font-size: 16px; line-height: 20px; color: var(--text-dark);
  }
  .required { font-size: 12px; color: var(--text-muted); }
  .field {
    position: absolute; border: 1px solid var(--field-border); border-radius: 3px; background: var(--white);
  }
  .consent-box {
    position: absolute; left: 127.5px; top: 486px; width: 19px; height: 19px;
    border: 1px solid var(--field-border); border-radius: 3px;
  }
  .consent-text {
    position: absolute; left: 159px; top: 485px; font-size: 16px; line-height: 20px; white-space: nowrap;
  }
  .notice-strip {
    position: absolute; left: 30px; top: 497px; width: 178px; height: 5px;
    background: var(--white); box-shadow: 0 -1px 3px rgba(0,0,0,0.2);
  }
</style>
</head>
<body>
  <header class="site-header">
    <div class="brand-name">Brunnkamp Maler</div>
    <nav class="main-nav">
      <a href="#">Home</a>
      <a href="#">Unsere Leistung</a>
      <a href="#" class="is-active">Kontakt</a>
    </nav>
    <div class="cta-button">Gespräch vereinbaren</div>
  </header>

  <main class="content-panel">
    <h1 class="page-title">Brunnkamp Maler</h1>
  </main>

  <label class="field-label" style="left:127.5px; top:207px;">Name</label>
  <div class="field" style="left:127.5px; top:237.5px; width:464px; height:43px;"></div>

  <label class="field-label" style="left:609px; top:207px;">E-Mail-Adresse <span class="required">(Pflichtfeld)</span></label>
  <div class="field" style="left:609px; top:237.5px; width:464px; height:43px;"></div>

  <label class="field-label" style="left:127.5px; top:304px;">Nachricht</label>
  <div class="field" style="left:127.5px; top:334px; width:945px; height:126px;"></div>

  <div class="consent-box"></div>
  <div class="consent-text">Ich habe die Datenschutzerklärung zur Kenntnis genommen und erkläre mich damit einverstanden. <span class="required">(Pflichtfeld)</span></div>

  <div class="notice-strip"></div>
</body>
</html>
```